Vendor Managed Inventory Talking points/Customer hand out

Looking for a single page flyer/Customer handout to be a sell sheet for our Vendor managed Inventory programs
Title: VMI benefits
Risk management:
Identification of Items and values that are sole sourced
Ongoing plans to reduce exposure to sole sourced items
Schedule planning to eliminate freight and outages
Reducing the hidden costs of forecasting errors
(Note; with us managing the point of use we can more accurately forecast)
Managing ever shortening of product lifecycles, minimizing obsolescence
Zero Inventory Exposure:
Minimized or Zero inventory on commodity items
Greatly reducing the Weighted Cost of Capital (WACC)
Reduced WACC can help in calculating Hurdle Rates
True point of use billing:
Allows for better tracking and allocation of expenses from a job-job basis
Custom labeling:
Including things like customer part numbers, exp dates, internal hazmat codes
Insures accurate processes with current materials
Helps to meet 5S requirements
Required for certain audits
Lot tracking/Shelf life:
Active assistance in managing Date Codes/Lot Tracking
Shortened shelf life products identified and managed
Plain statement of expiration dates on products. Calculations are not required
Taken as a whole we can help calculate TRUE management and landed costs of products. Focusing only on the price of items is like looking at just the exposed part of an iceberg. Let RT7K help you to see what's underneath.
I have attached some other brochures and flyers for style reference
more info on our website too. www.rt7k-example.com
Target Market(s)
Electronics manufacturers
Industry/Entity Type
Electronics
Look and feel

```html
<!DOCTYPE html>
<html lang="en">
<head>
<meta charset="utf-8">
<title>RT7K – VMI Benefits</title>
<link rel="stylesheet" href="https://fonts.googleapis.com/css2?family=Oswald:wght@500;700&family=Roboto:wght@400;700&display=swap">
<style>
  :root {
    --blue: #0a7fc9;
    --blue-dark: #0766a8;
    --ink: #1f1f1f;
    --black: #1b1b1b;
    --white: #ffffff;
    --page-bg: #8f8f8f;
    --photo-a: #6f7378;
    --photo-b: #2c2f33;
  }
  * { box-sizing: border-box; margin: 0; padding: 0; }
  html, body { width: 937px; height: 1200px; overflow: hidden; }
  body { background: var(--page-bg); font-family: "Roboto", Arial, sans-serif; color: var(--ink); position: relative; }
  .flyer { position: absolute; left: 65px; top: 76px; width: 808px; height: 1046px; background: var(--white); overflow: hidden; }
  .flyer-shapes { position: absolute; inset: 0; }
  .brand-name { position: absolute; left: 600px; top: 30px; width: 170px; text-align: center; font-family: "Oswald", sans-serif; font-weight: 700; font-size: 50px; color: var(--blue); letter-spacing: 1px; line-height: 1; }
  .title { position: absolute; left: 52px; top: 500px; font-family: "Oswald", sans-serif; font-weight: 700; font-size: 64px; letter-spacing: -0.5px; color: var(--black); line-height: 1; }
  .title .accent { color: var(--blue); }
  .benefit { position: absolute; }
  .benefit-icon { position: absolute; left: -52px; top: -6px; width: 44px; height: 44px; }
  .benefit h2 { font-family: "Oswald", sans-serif; font-weight: 500; font-size: 16px; color: var(--blue); letter-spacing: 0.2px; margin-bottom: 6px; text-transform: uppercase; }
  .benefit ul { list-style: none; }
  .benefit li { position: relative; padding-left: 11px; font-size: 12.3px; line-height: 15px; margin-bottom: 5px; }
  .benefit li::before { content: ""; position: absolute; left: 0; top: 4px; border-left: 5px solid var(--blue); border-top: 3.5px solid transparent; border-bottom: 3.5px solid transparent; }
  .benefit .note { padding-left: 11px; font-size: 12.3px; line-height: 15px; }
  .closing { position: absolute; left: 444px; top: 866px; width: 340px; font-weight: 700; font-size: 12.3px; line-height: 15px; }
  .contact { position: absolute; left: 30px; right: 30px; top: 1009px; display: flex; justify-content: space-between; align-items: center; color: var(--white); font-weight: 700; font-size: 14.5px; }
  .contact span { display: flex; align-items: center; gap: 6px; }
  .contact svg { width: 13px; height: 13px; }
</style>
</head>
<body>
<main class="flyer">
  <svg class="flyer-shapes" viewBox="0 0 808 1046" width="808" height="1046" aria-hidden="false">
    <defs>
      <linearGradient id="shelves" x1="0" y1="0" x2="1" y2="1">
        <stop offset="0" stop-color="var(--photo-a)"/>
        <stop offset="1" stop-color="var(--photo-b)"/>
      </linearGradient>
      <linearGradient id="staff" x1="0" y1="0" x2="0" y2="1">
        <stop offset="0" stop-color="#9aa4a0"/>
        <stop offset="1" stop-color="#c9d3dc"/>
      </linearGradient>
    </defs>
    <!-- header swooshes -->
    <path d="M0 0 H808 V420 C560 425 260 395 0 300 Z" fill="var(--blue)"/>
    <path d="M0 0 H808 V410 C560 412 250 390 0 320 Z" fill="var(--black)"/>
    <path d="M0 0 H808 V404 C560 408 260 370 30 250 C-5 160 0 60 0 0 Z" fill="var(--blue)"/>
    <path role="img" aria-label="Photo of storage shelves filled with labeled parts bins" d="M20 0 H808 V398 C560 402 280 365 70 250 C20 170 25 60 20 0 Z" fill="url(#shelves)"/>
    <!-- logo plate -->
    <ellipse cx="690" cy="60" rx="160" ry="78" fill="var(--white)"/>
    <!-- round photo -->
    <circle cx="614" cy="434" r="142" fill="var(--white)"/>
    <circle cx="614" cy="434" r="134" fill="url(#staff)" role="img" aria-label="Photo of a smiling staff member holding a tablet in a parts room"/>
    <!-- footer bands -->
    <path d="M0 920 C260 965 560 975 808 935 V1046 H0 Z" fill="var(--black)"/>
    <path d="M0 945 C260 985 560 992 808 955 V1046 H0 Z" fill="var(--blue)"/>
  </svg>

  <div class="brand-name">RT7K</div>

  <h1 class="title"><span class="accent">VMI</span> BENEFITS</h1>

  <section class="benefit" style="left:107px; top:597px; width:320px;">
    <svg class="benefit-icon" viewBox="0 0 44 44"><circle cx="22" cy="22" r="22" fill="var(--blue)"/><circle cx="22" cy="20" r="9" fill="none" stroke="#fff" stroke-width="1.6"/><path d="M13 20 H31 M22 11 V29 M15 31 L21 25 L25 28 L31 22" fill="none" stroke="#fff" stroke-width="1.6"/></svg>
    <h2>Risk Management</h2>
    <ul>
      <li>Identification of Items and values that are sole sourced</li>
      <li>Ongoing plans to reduce exposure to sole sourced items</li>
      <li>Schedule planning to eliminate freight and outages</li>
      <li>Reducing the hidden costs of forecasting errors</li>
    </ul>
    <p class="note">(Note; with us managing the point of use we can more accurately forecast)<br>Managing ever shortening of product lifecycles, minimizing obsolescence</p>
  </section>

  <section class="benefit" style="left:107px; top:770px; width:320px;">
    <svg class="benefit-icon" viewBox="0 0 44 44"><circle cx="22" cy="22" r="22" fill="var(--blue)"/><path d="M12 18 L22 13 L32 18 V28 L22 33 L12 28 Z M12 18 L22 23 L32 18 M22 23 V33" fill="none" stroke="#fff" stroke-width="1.6"/></svg>
    <h2>Zero Inventory Exposure</h2>
    <ul>
      <li>Minimized or Zero inventory on commodity items</li>
      <li>Greatly reducing the Weighted Cost of Capital (WACC)</li>
      <li>Reduced WACC can help in calculating Hurdle Rates</li>
    </ul>
  </section>

  <section class="benefit" style="left:107px; top:862px; width:320px;">
    <svg class="benefit-icon" viewBox="0 0 44 44"><circle cx="22" cy="22" r="22" fill="var(--blue)"/><rect x="14" y="11" width="16" height="22" fill="none" stroke="#fff" stroke-width="1.6"/><path d="M18 17 H26 M18 22 H26 M18 27 H24" stroke="#fff" stroke-width="1.6"/></svg>
    <h2>True Point of Use Billing</h2>
    <ul>
      <li>Allows for better tracking and allocation of expenses from a job-job basis</li>
    </ul>
  </section>

  <section class="benefit" style="left:490px; top:592px; width:290px;">
    <svg class="benefit-icon" viewBox="0 0 44 44"><circle cx="22" cy="22" r="22" fill="var(--blue)"/><rect x="12" y="15" width="20" height="14" rx="2" fill="none" stroke="#fff" stroke-width="1.6"/><circle cx="16" cy="22" r="1.6" fill="#fff"/></svg>
    <h2>Custom Labeling</h2>
    <ul>
      <li>Including things like customer part numbers, exp dates, internal hazmat codes</li>
      <li>Insures accurate processes with current materials</li>
      <li>Helps to meet 5S requirements</li>
      <li>Required for certain audits</li>
    </ul>
  </section>

  <section class="benefit" style="left:490px; top:735px; width:290px;">
    <svg class="benefit-icon" viewBox="0 0 44 44"><circle cx="22" cy="22" r="22" fill="var(--blue)"/><path d="M22 34 C15 26 13 22 13 18 A9 9 0 0 1 31 18 C31 22 29 26 22 34 Z" fill="none" stroke="#fff" stroke-width="1.6"/><circle cx="22" cy="18" r="3.5" fill="none" stroke="#fff" stroke-width="1.6"/></svg>
    <h2>Lot Tracking/Shelf Life</h2>
    <ul>
      <li>Active assistance in managing Date Codes/Lot Tracking</li>
      <li>Shortened shelf life products identified and managed</li>
      <li>Plain statement of expiration dates on products. Calculations are not required</li>
    </ul>
  </section>

  <p class="closing">Taken as a whole we can help calculate TRUE management and landed costs of products. Focusing only on the price of items is like looking at just the exposed part of an iceberg. Let RT7K help you to see what’s underneath.</p>

  <footer class="contact">
    <span><svg viewBox="0 0 13 13"><circle cx="6.5" cy="6.5" r="6.5" fill="var(--blue-dark)"/><path d="M3.5 7 L6.5 4 L9.5 7 V9.5 H3.5 Z" fill="#fff"/></svg>140 Alder Lane Millbrook,PA 17000</span>
    <span><svg viewBox="0 0 13 13"><circle cx="6.5" cy="6.5" r="6.5" fill="var(--blue-dark)"/><path d="M4 3.5 L5.5 3.5 L6 5.5 L5 6.2 A5 5 0 0 0 6.8 8 L7.5 7 L9.5 7.5 V9 C6 9.5 3.5 7 4 3.5 Z" fill="#fff"/></svg>800.555.0142</span>
    <span><svg viewBox="0 0 13 13"><circle cx="6.5" cy="6.5" r="6.5" fill="var(--blue-dark)"/><rect x="3.5" y="4.5" width="6" height="4" fill="#fff"/></svg>Sales@rt7k-example.com</span>
    <span><svg viewBox="0 0 13 13"><circle cx="6.5" cy="6.5" r="6.5" fill="var(--blue-dark)"/><circle cx="6.5" cy="6.5" r="3" fill="none" stroke="#fff" stroke-width="1"/></svg>www.rt7k-example.com</span>
  </footer>
</main>
</body>
</html>
```